Spice Mix Label Bottle Branding - Health and Weight Loss Mixes

The company is called ZestoLane Spice Mix's. We've created 5 spice mixes using ingredients that promote health and weight loss. We already have a logo but now we need labels for our bottles. We would like to see designs that have the feel of health supplements (see attached examples)

We would like a different colour featured with each of our flavours.

Our flavours are:
-Golden Chai (Yellow)
-Mild Curry (Orange)
-Coffee Rub (brown)
-Garlic Oregano (Green)
-Taco (Blue)

Thank you!

Target Market(s)

Ages 22-35. Men and Female. Trendy, Hipster.

Industry/Entity Type

Food Production

Font styles to use
Sans Serif

Colors
f37122
0655a3
0692cd
9bcb3c
fbee3f

Requirements
Must have
• A different featured colour for each flavour.
• The ZestoLane Spices Logo (attached)
• The slogan: "Weight Loss Ingredients"
• -Golden Chai (Yellow)
• -Mild Curry (Orange)
• -Coffee Rub (brown)
• -Garlic Oregano (Green)
• -Taco (Blue)
• Text Files attached.
Nice to have
• A black label with a featured colour for each of the spice mice flavours.
• 'No Salt added'

```html
<!DOCTYPE html>
<html lang="en">
<head>
<meta charset="utf-8">
<title>ZestoLane Spices – Flavour Labels</title>
<link rel="stylesheet" href="https://fonts.googleapis.com/css2?family=Bebas+Neue&family=Bangers&display=swap">
<style>
  :root {
    --paper: #ffffff;
    --label-black: #000000;
    --ink-dark: #141414;
    --ink-light: #ffffff;
    --chai: #d6a02e;
    --chai-ribbon: #e0b043;
    --curry: #ec5424;
    --curry-ribbon: #f37122;
    --oregano: #97b83a;
    --oregano-ribbon: #9bcb3c;
    --coffee: #9c652d;
    --coffee-ribbon: #b07d43;
    --taco: #336ea9;
    --taco-ribbon: #3f92d2;
  }
  html, body {
    margin: 0;
    padding: 0;
    width: 875px;
    height: 1200px;
    overflow: hidden;
    background: var(--paper);
  }
  .label-sheet { display: block; }
  .label-strip { fill: var(--label-black); }
  .badge-ring {
    fill: none;
    stroke: var(--tone);
    stroke-width: 18;
  }
  .ribbon {
    fill: var(--ribbon);
    stroke: var(--tone);
    stroke-width: 1.5;
  }
  .flavour-name {
    font-family: "Bangers", sans-serif;
    font-size: 24px;
    letter-spacing: 1px;
    fill: var(--ink-dark);
  }
  .rule { stroke: var(--tone); stroke-width: 1; }
  .rule-dot { fill: var(--tone); }
  .brand-name {
    font-family: "Bebas Neue", sans-serif;
    fill: var(--ink-light);
  }
  .brand-word { font-size: 58px; }
  .brand-sub { font-size: 13px; letter-spacing: 9px; }
  .no-salt {
    font-family: "Bebas Neue", sans-serif;
    font-size: 13px;
    letter-spacing: 0.6px;
    fill: var(--ink-light);
  }
  .slogan {
    font-family: "Bangers", sans-serif;
    font-size: 12.5px;
    letter-spacing: 0.4px;
    fill: var(--ink-dark);
  }
</style>
</head>
<body>
<svg class="label-sheet" width="875" height="1200" viewBox="0 0 875 1200" xmlns="http://www.w3.org/2000/svg">
  <defs>
    <path id="ribbon-curve" d="M -88,-64 Q 0,-106 88,-64"/>
    <path id="slogan-curve" d="M -89.2,51.5 A 103 103 0 0 0 89.2,51.5"/>
    <g id="badge-body">
      <path class="badge-ring" d="M -92.6,-32 A 98 98 0 0 1 92.6,-32"/>
      <path class="badge-ring" d="M 93.9,28 A 98 98 0 0 1 -93.9,28"/>
      <path class="ribbon" d="M -96,-84 Q 0,-132 96,-84 L 86,-50 Q 0,-92 -86,-50 Z"/>
      <line class="rule" x1="-86" y1="-34" x2="-28" y2="-34"/>
      <line class="rule" x1="28" y1="-34" x2="86" y2="-34"/>
      <circle class="rule-dot" cx="-86" cy="-34" r="1.6"/>
      <circle class="rule-dot" cx="86" cy="-34" r="1.6"/>
      <text class="brand-name brand-word" x="0" y="22" text-anchor="middle" textLength="150" lengthAdjust="spacingAndGlyphs">ZestoLane</text>
      <text class="brand-name brand-sub" x="4" y="41" text-anchor="middle">SPICES</text>
      <text class="no-salt" x="0" y="57" text-anchor="middle">No Salt Added</text>
      <line class="rule" x1="-42" y1="62" x2="42" y2="62"/>
      <circle class="rule-dot" cx="-4" cy="65.5" r="1.3"/>
      <circle class="rule-dot" cx="0" cy="65.5" r="1.3"/>
      <circle class="rule-dot" cx="4" cy="65.5" r="1.3"/>
      <text class="slogan"><textPath href="#slogan-curve" startOffset="50%" text-anchor="middle">• Weight Loss Ingredients •</textPath></text>
    </g>
  </defs>

  <g class="label label--golden-chai" style="--tone: var(--chai); --ribbon: var(--chai-ribbon);">
    <rect class="label-strip" x="13" y="14" width="849" height="232"/>
    <g transform="translate(437 131)">
      <use href="#badge-body"/>
      <text class="flavour-name"><textPath href="#ribbon-curve" startOffset="50%" text-anchor="middle">GOLDEN CHAI</textPath></text>
    </g>
  </g>

  <g class="label label--mild-curry" style="--tone: var(--curry); --ribbon: var(--curry-ribbon);">
    <rect class="label-strip" x="13" y="247" width="849" height="232"/>
    <g transform="translate(437 364)">
      <use href="#badge-body"/>
      <text class="flavour-name"><textPath href="#ribbon-curve" startOffset="50%" text-anchor="middle">MILD CURRY</textPath></text>
    </g>
  </g>

  <g class="label label--garlic-oregano" style="--tone: var(--oregano); --ribbon: var(--oregano-ribbon);">
    <rect class="label-strip" x="13" y="480" width="849" height="232"/>
    <g transform="translate(437 597)">
      <use href="#badge-body"/>
      <text class="flavour-name"><textPath href="#ribbon-curve" startOffset="50%" text-anchor="middle">GARLIC OREGANO</textPath></text>
    </g>
  </g>

  <g class="label label--coffee-rub" style="--tone: var(--coffee); --ribbon: var(--coffee-ribbon);">
    <rect class="label-strip" x="13" y="713" width="849" height="232"/>
    <g transform="translate(437 830)">
      <use href="#badge-body"/>
      <text class="flavour-name"><textPath href="#ribbon-curve" startOffset="50%" text-anchor="middle">COFFEE RUB</textPath></text>
    </g>
  </g>

  <g class="label label--taco" style="--tone: var(--taco); --ribbon: var(--taco-ribbon);">
    <rect class="label-strip" x="13" y="946" width="849" height="232"/>
    <g transform="translate(437 1063)">
      <use href="#badge-body"/>
      <text class="flavour-name"><textPath href="#ribbon-curve" startOffset="50%" text-anchor="middle">TACO</textPath></text>
    </g>
  </g>
</svg>
</body>
</html>
```